Solace Chiropractic & Acupuncture Business Cards

I need a business card design that feels elevated. I am open to any of the logo designs uploaded. We have two doctors so I'll need to be able to change out the names.

Information:
Marnie Toller D.C., Dipl. Ac. ASA
584 W 12th St, Ste 320
Hutchinson, KS 67419
solacegrove.net
620-555-0147
drmarnie@solacegrove.com
Updates

We have designs we like now, we are just trying to choose between top contenders. Thanks for your submissions!

Contact Information for Business Card

noted in description

Requirements
Must have
• ability to edit info if possible
Nice to have
• Please see our website solacegrove.net for our style and colors

```html
<!DOCTYPE html>
<html lang="en">
<head>
<meta charset="utf-8">
<title>Solace Chiropractic &amp; Acupuncture — Business Cards</title>
<link rel="stylesheet" href="https://fonts.googleapis.com/css2?family=Cormorant+Garamond:wght@500&family=Playfair+Display:wght@700&family=Poppins:wght@400&display=swap">
<style>
  :root {
    --backdrop: #2a2a2c;
    --card-navy: #3a4257;
    --card-white: #ffffff;
    --ink-navy: #2c3449;
    --ink-soft: #3d4459;
    --mark-light: #c9cede;
    --rule: #4a5166;
  }
  * { box-sizing: border-box; margin: 0; padding: 0; }
  html, body {
    width: 1200px; height: 900px; overflow: hidden;
    background: var(--backdrop);
  }
  .canvas { position: relative; width: 1200px; height: 900px; }

  .card {
    position: absolute;
    width: 630px; height: 360px;
    border-radius: 22px;
    box-shadow: 0 18px 40px rgba(0,0,0,.45);
  }

  /* Front: brand face */
  .card-front {
    left: 470px; top: 60px;
    background: var(--card-navy);
    display: flex; flex-direction: column;
    align-items: center; justify-content: center;
  }
  .brand-name {
    font-family: "Cormorant Garamond", serif;
    font-weight: 500;
    color: var(--mark-light);
    text-align: center;
    line-height: 1.05;
  }
  .card-front .brand-name { font-size: 96px; }
  .card-front .brand-tagline {
    font-family: "Cormorant Garamond", serif;
    font-weight: 500;
    color: var(--mark-light);
    font-size: 24px;
    letter-spacing: 3px;
    text-transform: uppercase;
    margin-top: 6px;
  }

  /* Back: contact face */
  .card-back {
    left: 100px; top: 480px;
    background: var(--card-white);
    display: flex; align-items: center;
  }
  .brand-block {
    width: 250px;
    display: flex; flex-direction: column; align-items: center;
    gap: 12px;
  }
  .brand-dot {
    width: 14px; height: 14px; border-radius: 50%;
    background: var(--ink-navy);
  }
  .card-back .brand-name {
    color: var(--ink-navy);
    font-size: 44px;
    letter-spacing: 4px;
    text-transform: uppercase;
  }
  .card-back .brand-tagline {
    font-family: "Cormorant Garamond", serif;
    font-weight: 500;
    color: var(--ink-navy);
    font-size: 19px;
    text-transform: uppercase;
    text-align: center;
    line-height: 1.1;
  }
  .divider {
    width: 1.5px; height: 190px;
    background: var(--rule);
    margin: 0 36px 0 20px;
  }
  .contact-block { color: var(--ink-soft); font-family: "Poppins", sans-serif; }
  .doctor-name {
    font-family: "Playfair Display", serif;
    font-weight: 700;
    font-size: 25px;
    letter-spacing: 2px;
    text-transform: uppercase;
    color: var(--ink-navy);
  }
  .credentials { font-size: 14px; margin-bottom: 14px; }
  .address { font-size: 15px; line-height: 1.3; margin-bottom: 14px; }
  .contact-list { list-style: none; font-size: 15px; line-height: 1.45; }
  .contact-list li { display: flex; align-items: center; gap: 10px; }
  .contact-list svg { width: 13px; height: 13px; fill: var(--ink-navy); flex: none; }
</style>
</head>
<body>
<main class="canvas">

  <section class="card card-front" aria-label="Card front">
    <div class="brand-name">Solace</div>
    <div class="brand-tagline">Chiropractic &amp; Acupuncture</div>
  </section>

  <section class="card card-back" aria-label="Card back">
    <div class="brand-block">
      <span class="brand-dot"></span>
      <div class="brand-name">Solace</div>
      <div class="brand-tagline">Chiropractic<br>&amp; Acupuncture</div>
    </div>

    <div class="divider"></div>

    <div class="contact-block">
      <h1 class="doctor-name">Marnie Toller</h1>
      <p class="credentials">D.C., Dipl. Ac. ASA</p>
      <p class="address">584 W 12th St, Ste 320<br>Hutchinson, KS 67419</p>
      <ul class="contact-list">
        <li>
          <svg viewBox="0 0 16 16" aria-hidden="true"><path d="M3 1h3l1.5 4-2 1.3a9 9 0 0 0 4.2 4.2L11 8.5l4 1.5v3a2 2 0 0 1-2 2A12 12 0 0 1 1 3a2 2 0 0 1 2-2z"/></svg>
          620-555-0147
        </li>
        <li>
          <svg viewBox="0 0 16 16" aria-hidden="true"><path d="M1 3h14v1.2L8 9 1 4.2z"/><path d="M1 5.8 8 10.6l7-4.8V13H1z"/></svg>
          drmarnie@solacegrove.com
        </li>
        <li>
          <svg viewBox="0 0 16 16" aria-hidden="true"><circle cx="8" cy="8" r="7"/></svg>
          www.solacegrove.net
        </li>
      </ul>
    </div>
  </section>

</main>
</body>
</html>
```